Graphic picture for front page of website

We need a picture to place on the front page of our wordpress Website. The company name is Brindle Cells , and we sell Quorvane Ledger services. The website is www.brindlecells-demo.com . I am looking for something to go in the picture in the middle of the site, to replace the current default template. Currently we use the color green, as it is default, but happy for you to be creative to see what works (colorful is good). I have included just some random screenshots of projects I have done for clients, for some possible inspiration. Have a look at our services to see what kinds of work we do.
We currently have no logo, the tolmir thing is just a default of the wordpress theme.
Hi guys, I have uploaded a picture to show you the dimensions (the ratio, please make the image large so it is very high quality, i can scale it to the exact size needed). All of the writing/key info should be in the red lines, people with smaller monitors will just see that, people with wide monitors will see all of it.
Thanks
No stock photos of people thanks.
Small to large business, looking for Quorvane Ledger services.
It Company

```html
<!DOCTYPE html>
<html lang="en">
<head>
<meta charset="utf-8">
<title>Brindle Cells – Spreadsheet Tools Banners</title>
<link rel="stylesheet" href="https://fonts.googleapis.com/css2?family=Barlow+Semi+Condensed:wght@600&family=Barlow:wght@500&display=swap">
<style>
  :root {
    --page-bg: #dcdcdc;
    --red: #c4001f;
    --red-dark: #9a0c2e;
    --magenta: #ec1a86;
    --maroon: #8e2456;
    --blue: #1a2f9c;
    --blue-dark: #0f1d6e;
    --cyan: #3fd9f2;
    --green: #0b8a2e;
    --green-dark: #066b22;
    --mint: #22e27a;
    --yellow: #ffe800;
    --amber: #f7a21c;
    --white: #ffffff;
  }
  * { margin: 0; padding: 0; box-sizing: border-box; }
  html, body { width: 1200px; height: 1000px; overflow: hidden; background: var(--page-bg); }
  .canvas { position: relative; width: 1200px; height: 1000px; }
  .banner { position: absolute; left: 214px; width: 772px; height: 296px; overflow: hidden; background: var(--white); }
  .banner--macro { top: 45px; }
  .banner--daily { top: 353px; }
  .banner--weekly { top: 661px; }

  .banner__shot { position: absolute; top: 0; right: 0; height: 296px; }
  .banner--macro .banner__shot {
    left: 250px;
    background: linear-gradient(120deg, #ffffff 0%, #fbf6cf 35%, #f7d25a 55%, #efa73a 70%, #ffffff 92%);
  }
  .banner--daily .banner__shot {
    left: 200px;
    background: linear-gradient(165deg, #eef1f6 0%, #1f3585 16%, #f3f6fb 24%, #f6b0a6 48%, #b8efc0 66%, #ffffff 90%);
  }
  .banner--weekly .banner__shot {
    left: 190px;
    background: linear-gradient(170deg, #f1f1f1 0%, #1f3585 14%, #5fcaf0 22%, #d8eef9 45%, #ffffff 90%);
  }

  .banner__field { position: absolute; inset: 0; width: 772px; height: 296px; display: block; }

  .banner__copy { position: absolute; left: 89px; color: var(--white); }
  .banner--macro .banner__copy { top: 89px; }
  .banner--daily .banner__copy { top: 107px; }
  .banner--weekly .banner__copy { top: 102px; }
  .banner__title {
    font-family: "Barlow Semi Condensed", "Arial Narrow", sans-serif;
    font-weight: 600; font-size: 37px; line-height: 36px;
  }
  .banner__title span { display: block; }
  .accent-yellow { color: var(--yellow); }
  .accent-amber { color: var(--amber); }
  .banner__text {
    margin-top: 14px; width: 200px;
    font-family: "Barlow", Arial, sans-serif; font-weight: 500; font-size: 10.5px; line-height: 14px;
  }
</style>
</head>
<body>
<div class="canvas">

  <section class="banner banner--macro">
    <div class="banner__shot" role="img" aria-label="Spreadsheet screenshot of a beam sizing macro with a yellow and orange span chart"></div>
    <svg class="banner__field" viewBox="0 0 772 296" xmlns="http://www.w3.org/2000/svg" aria-hidden="true">
      <polygon points="0,0 260,0 430,296 0,296" fill="var(--red)"/>
      <polygon points="170,0 262,0 320,110" fill="var(--maroon)" opacity="0.9"/>
      <polygon points="262,0 300,0 440,296 402,296" fill="var(--magenta)"/>
      <polygon points="240,0 262,0 420,296 395,296" fill="#d8125a" opacity="0.8"/>
      <polygon points="0,120 140,296 0,296" fill="var(--red-dark)" opacity="0.35"/>
      <polygon points="0,200 70,296 0,296" fill="var(--red-dark)" opacity="0.4"/>
    </svg>
    <div class="banner__copy">
      <h2 class="banner__title"><span>RUN</span><span class="accent-yellow">MARCO</span></h2>
      <p class="banner__text">Lorem Ipsum is simply dummy text of the printing and typesetting industry.</p>
    </div>
  </section>

  <section class="banner banner--daily">
    <div class="banner__shot" role="img" aria-label="Spreadsheet screenshot of a daily planner with coloured task bars across hourly columns"></div>
    <svg class="banner__field" viewBox="0 0 772 296" xmlns="http://www.w3.org/2000/svg" aria-hidden="true">
      <polygon points="0,0 150,0 365,296 0,296" fill="var(--blue)"/>
      <polygon points="150,0 200,0 420,296 365,296" fill="var(--cyan)"/>
      <polygon points="200,0 215,0 440,296 420,296" fill="#2a7ae0" opacity="0.6"/>
      <polygon points="120,0 150,0 365,296 330,296" fill="#2848c8" opacity="0.8"/>
      <polygon points="0,150 110,296 0,296" fill="var(--blue-dark)" opacity="0.6"/>
      <polygon points="0,230 50,296 0,296" fill="#060d3c" opacity="0.7"/>
    </svg>
    <div class="banner__copy">
      <h2 class="banner__title"><span>DAILY WEEK</span><span class="accent-amber">PLANNER</span></h2>
      <p class="banner__text">Lorem Ipsum is simply dummy text of the printing and typesetting industry.</p>
    </div>
  </section>

  <section class="banner banner--weekly">
    <div class="banner__shot" role="img" aria-label="Spreadsheet screenshot of a two-week staff shift planner grid"></div>
    <svg class="banner__field" viewBox="0 0 772 296" xmlns="http://www.w3.org/2000/svg" aria-hidden="true">
      <polygon points="0,0 150,0 360,296 0,296" fill="var(--green)"/>
      <polygon points="150,0 205,0 430,296 360,296" fill="var(--mint)"/>
      <polygon points="205,0 225,0 440,296 430,296" fill="#7cf0b0" opacity="0.7"/>
      <polygon points="110,0 150,0 360,296 320,296" fill="#14b84a" opacity="0.7"/>
      <polygon points="0,130 120,296 0,296" fill="var(--green-dark)" opacity="0.6"/>
      <polygon points="0,220 55,296 0,296" fill="#034d16" opacity="0.7"/>
    </svg>
    <div class="banner__copy">
      <h2 class="banner__title"><span>WEEKLY</span><span class="accent-yellow">PLANNER</span></h2>
      <p class="banner__text">Lorem Ipsum is simply dummy text of the printing and typesetting industry.</p>
    </div>
  </section>

</div>
</body>
</html>
```